Personal creative Biz Card Design

Need personal yet natural and organic design. The cards I have now are well designed but look too commercial. I want more organic FEELING kind of card. I thought having a headshot would make it more personal... but maybe a sketch effect (or line drawing effect) of face better (?). Maybe in a gray or tungsten color?

Target Market(s)

Well, everyone i give card to will have already seen me face-to-face so that is one thing. Mostly yoga students and people interested in improving their fitness or general health. People looking for wellness, a personal fitness trainer, a yoga teacher

Industry/Entity Type

Health And Wellness

Contact Information for Business Card

I provided examples

Requirements
Must have
• My main logo
• My name

```html
<!DOCTYPE html>
<html lang="en">
<head>
<meta charset="utf-8">
<title>Noel Farrow – Business Cards</title>
<link rel="stylesheet" href="https://fonts.googleapis.com/css2?family=Montserrat:wght@400;600&family=Courier+Prime:wght@700&display=swap">
<style>
  :root {
    --page-bg: #e9eaea;
    --ink-gray: #5d6366;
    --paper: #ffffff;
    --paper-shade: #e4e6e6;
    --card-w: 525px;
    --card-h: 300px;
  }
  .palette-green {
    --accent: #8cc63f;
    --accent-deep: #5f9a22;
    --accent-light: #a9d86a;
    --band: #151515;
    --band-text: #a9d86a;
  }
  .palette-gray {
    --accent: #8e9193;
    --accent-deep: #55595b;
    --accent-light: #c9cbcc;
    --band: #1c1c1c;
    --band-text: #d6d8d9;
  }
  * { box-sizing: border-box; margin: 0; padding: 0; }
  html, body {
    width: 1200px; height: 960px; overflow: hidden;
    background: var(--page-bg);
    font-family: "Montserrat", sans-serif;
  }
  .sheet {
    width: 1200px; height: 960px;
    display: flex; flex-direction: column; justify-content: center;
    gap: 120px; padding: 0 55px;
  }
  .card-row { display: flex; gap: 40px; }
  .card {
    position: relative; width: var(--card-w); height: var(--card-h);
    overflow: hidden;
    box-shadow: 0 2px 6px rgba(0,0,0,.18);
  }

  /* Front */
  .card-front { background: linear-gradient(135deg, var(--paper) 40%, var(--paper-shade)); }
  .front-sweep { position: absolute; inset: 0; }
  .front-sweep .sweep-fill { fill: var(--accent); }
  .front-sweep .sweep-edge { fill: none; stroke: var(--paper); stroke-width: 3; }
  .identity {
    position: absolute; left: 34px; top: 62px;
    display: flex; align-items: center; gap: 14px;
  }
  .identity-dot {
    width: 46px; height: 46px; border-radius: 50%;
    background: var(--accent);
  }
  .identity-name {
    font-weight: 600; font-size: 34px; letter-spacing: 1px;
    color: var(--ink-gray); line-height: 1;
  }
  .tagline {
    position: absolute; left: 96px; top: 104px;
    font-size: 11px; color: var(--accent-deep); letter-spacing: .3px;
  }
  .phone {
    position: absolute; right: 16px; top: 10px;
    display: flex; align-items: center; gap: 6px;
    font-size: 12px; color: var(--ink-gray); letter-spacing: 1px;
  }
  .phone-icon { width: 16px; height: 16px; }
  .phone-icon circle { fill: var(--ink-gray); }
  .phone-icon path { fill: var(--paper); }
  .front-contact {
    position: absolute; left: 150px; bottom: 22px; text-align: left;
    color: var(--paper);
  }
  .web {
    font-family: "Courier Prime", monospace; font-weight: 700;
    font-size: 24px; letter-spacing: 2px; line-height: 1.1;
  }
  .email { font-size: 16px; letter-spacing: 2px; }

  /* Back */
  .card-back {
    background: radial-gradient(ellipse at 45% 30%, var(--accent-light), var(--accent) 55%, var(--accent-deep));
  }
  .back-band {
    position: absolute; left: 0; right: 0; bottom: 0; height: 96px;
    background: var(--band);
    border-top: 3px solid var(--paper);
  }
  .back-mark {
    position: absolute; left: 0; right: 0; top: 70px;
    display: flex; justify-content: center; align-items: center; gap: 12px;
  }
  .back-mark .identity-dot { background: var(--paper); width: 34px; height: 34px; }
  .back-mark .identity-name { color: var(--paper); font-size: 26px; }
  .back-contact {
    position: absolute; left: 0; right: 0; bottom: 18px;
    text-align: center; color: var(--band-text);
  }
  .back-contact .web { font-size: 21px; }
  .back-contact .email { font-size: 15px; }
</style>
</head>
<body>
<main class="sheet">

  <section class="card-row palette-green">
    <article class="card card-front">
      <svg class="front-sweep" viewBox="0 0 525 300" preserveAspectRatio="none">
        <path class="sweep-fill" d="M0,190 C220,185 400,140 525,20 L525,300 L0,300 Z"/>
        <path class="sweep-edge" d="M0,190 C220,185 400,140 525,20"/>
      </svg>
      <div class="phone">
        <svg class="phone-icon" viewBox="0 0 16 16"><circle cx="8" cy="8" r="8"/><path d="M5 4l2 0 1 2-1 1c.5 1 1.2 1.7 2 2l1-1 2 1v2c-4 .5-7.5-3-7-7z"/></svg>
        <span>555-201-3478</span>
      </div>
      <div class="identity">
        <span class="identity-dot"></span>
        <h1 class="identity-name">NOEL FARROW</h1>
      </div>
      <p class="tagline">Expert Guidance for a Healthier Life</p>
      <div class="front-contact">
        <p class="web">www.noelfarrow.com</p>
        <p class="email">noelstillpaths@mail.com</p>
      </div>
    </article>
    <article class="card card-back">
      <div class="back-mark">
        <span class="identity-dot"></span>
        <span class="identity-name">NOEL FARROW</span>
      </div>
      <div class="back-band"></div>
      <div class="back-contact">
        <p class="web">www.noelfarrow.com</p>
        <p class="email">noelstillpaths@mail.com</p>
      </div>
    </article>
  </section>

  <section class="card-row palette-gray">
    <article class="card card-front">
      <svg class="front-sweep" viewBox="0 0 525 300" preserveAspectRatio="none">
        <path class="sweep-fill" d="M0,190 C220,185 400,140 525,20 L525,300 L0,300 Z"/>
        <path class="sweep-edge" d="M0,190 C220,185 400,140 525,20"/>
      </svg>
      <div class="phone">
        <svg class="phone-icon" viewBox="0 0 16 16"><circle cx="8" cy="8" r="8"/><path d="M5 4l2 0 1 2-1 1c.5 1 1.2 1.7 2 2l1-1 2 1v2c-4 .5-7.5-3-7-7z"/></svg>
        <span>555-201-3478</span>
      </div>
      <div class="identity">
        <span class="identity-dot"></span>
        <h2 class="identity-name">NOEL FARROW</h2>
      </div>
      <p class="tagline">Expert Guidance for a Healthier Life</p>
      <div class="front-contact">
        <p class="web">www.noelfarrow.com</p>
        <p class="email">noelstillpaths@mail.com</p>
      </div>
    </article>
    <article class="card card-back">
      <div class="back-mark">
        <span class="identity-dot"></span>
        <span class="identity-name">NOEL FARROW</span>
      </div>
      <div class="back-band"></div>
      <div class="back-contact">
        <p class="web">www.noelfarrow.com</p>
        <p class="email">noelstillpaths@mail.com</p>
      </div>
    </article>
  </section>

</main>
</body>
</html>
```